Web site design for Brivolt Software (www.brivoltsoftware-example.com)

Need the design as well as the html for the website. The brief is given in the attached file.
If possible, would like to use pencil sketches instead of images to give a unique look to the site.
Target Market(s)
small Software product companies
Industry/Entity Type
Software
Coding
Coded - Design and coding required
Number of Pages Required
5+ page

```html
<!DOCTYPE html>
<html lang="en">
<head>
<meta charset="utf-8">
<title>Brivolt Software — Driven by architecture</title>
<link href="https://fonts.googleapis.com/css2?family=Courier+Prime:wght@400;700&family=Special+Elite&family=Lato:wght@400&display=swap" rel="stylesheet">
<style>
:root{
  --ink:#0b0b0b;
  --night:#151515;
  --paper:#f4f4f0;
  --text:#e9e9e6;
  --muted:#b9b9b4;
  --accent:#e0742a;
  --sketch:#3a3a3a;
  --kraft:#c9a066;
}
*{margin:0;padding:0;box-sizing:border-box}
html,body{width:1200px;height:2635px;overflow:hidden;background:var(--ink)}
body{position:relative;font-family:"Courier Prime",monospace;color:var(--text)}
.abs{position:absolute}
.nav{top:48px;font-family:"Courier Prime",monospace;font-size:14px;color:var(--text);display:flex;gap:24px}
.nav-left{left:16px}
.nav-right{right:16px}
.brand{left:395px;top:36px;width:410px;height:58px;border:1px solid #555;text-align:center}
.brand-name{font-family:"Special Elite",monospace;font-size:44px;letter-spacing:6px;color:var(--paper);line-height:56px}
.tagline{left:0;width:1200px;top:86px;text-align:center;font-size:17px;color:var(--muted);letter-spacing:1px}
.tagline span{background:var(--ink);padding:0 8px}
.label{left:0;width:1200px;text-align:center}
.label span{display:inline-block;background:var(--paper);color:var(--ink);font-family:"Special Elite",monospace;font-size:19px;padding:4px 16px}
.sub{left:0;width:1200px;text-align:center;font-size:15px}
.rule{left:525px;width:150px;height:1px;background:#777}
.para{left:90px;width:1020px;text-align:center;font-size:14.5px;line-height:25px}
.services{left:100px;width:1000px;top:665px;display:flex;justify-content:space-between}
.service{text-align:center;font-size:15px}
.service svg{display:block;margin:0 auto 8px}
.arrow{color:var(--paper)}
.expertise{left:46px;top:968px;width:628px;font-size:19px;line-height:30px;text-align:justify}
.wanted{left:128px;top:1400px;width:450px;height:197px;background:linear-gradient(135deg,#d5b07a,var(--kraft) 55%,#a57a44);border:1px solid #8a6a3c}
.wanted-title{position:absolute;left:0;top:14px;width:100%;text-align:center;font-family:"Special Elite",monospace;font-size:30px;color:#2a1d0e}
.wanted-text{position:absolute;left:20px;top:62px;width:415px;font-size:13.5px;line-height:20px;color:#3b2a15}
.work{left:632px;top:1392px;width:500px;font-size:19px;line-height:30px}
.btn{left:636px;top:1543px;width:188px;height:35px;background:var(--paper);color:var(--ink);font-family:"Special Elite",monospace;font-size:18px;text-align:center;line-height:35px}
.quote{left:300px;width:600px;top:1845px;text-align:center;font-size:14px;line-height:22px;color:var(--muted)}
.qmark{font-size:26px;color:var(--paper);top:1862px}
.client{left:0;width:1200px;text-align:center}
.portrait{top:2027px;width:104px;height:104px;background:linear-gradient(160deg,#777,#2d2d2d)}
.contact{top:2358px;display:flex;gap:18px}
.contact .dot{width:42px;height:42px;border-radius:50%;background:var(--paper);display:flex;align-items:center;justify-content:center;flex:none}
.contact h3{font-family:"Courier Prime",monospace;font-weight:400;font-size:18px;color:var(--paper);margin-top:0}
.contact p{font-size:13px;line-height:26px;color:var(--muted)}
.divider{left:60px;width:1080px;top:2545px;height:1px;background:#333}
.copy{left:0;width:1200px;top:2578px;text-align:center;font-family:"Lato",sans-serif;font-size:12px;color:var(--muted)}
</style>
</head>
<body>

<div class="abs" role="img" aria-label="Pencil sketch of a gothic tower and bridge" style="left:760px;top:80px;width:440px;height:620px;background:radial-gradient(ellipse at 60% 40%,#2b2b2b,transparent 70%)"></div>
<div class="abs" role="img" aria-label="Faint photo of a person working at dusk" style="left:160px;top:700px;width:360px;height:300px;background:radial-gradient(ellipse at 50% 50%,#2a1d12,transparent 70%)"></div>
<div class="abs" role="img" aria-label="Dark photo of a gothic cathedral facade" style="left:0;top:1860px;width:1200px;height:775px;background:linear-gradient(180deg,transparent,#1c1c1c 30%,#262626 70%,#1a1a1a)"></div>

<nav class="abs nav nav-left"><span>Home</span><span>About Us</span><span>Services</span><span>Expertise</span><span>Stories</span></nav>
<nav class="abs nav nav-right"><span>Engagement Models</span><span>Agile</span><span>Case studies</span><span>Contact</span></nav>
<div class="abs brand"><div class="brand-name">BRIVOLT</div></div>
<div class="abs tagline"><span>• Driven By architecture •</span></div>

<div class="abs label" style="top:198px"><span>About Us</span></div>
<div class="abs sub" style="top:242px">We are passionate</div>
<div class="abs rule" style="top:268px"></div>
<p class="abs para" style="top:286px">in our belief that a software product's architecture goes a long way in avoiding costly and complex upgrades. Our architecture driven approach makes sure that product upgrades are possible while maintaining productive and friendly user interfaces.</p>
<p class="abs para" style="top:385px">Whether you are an established software product development company, a startup company or just a person with an idea, we would love to work with you. We work closely with clients to develop top level requirements, design the right team, and implement the software.</p>

<div class="abs label" style="top:568px"><span>Services</span></div>
<svg class="abs arrow" style="left:35px;top:704px" width="52" height="20" viewBox="0 0 52 20"><path d="M50 10H4M12 2L3 10l9 8" fill="none" stroke="#f4f4f0" stroke-width="3"/></svg>
<svg class="abs arrow" style="left:1103px;top:704px" width="52" height="20" viewBox="0 0 52 20"><path d="M2 10h46M40 2l9 8-9 8" fill="none" stroke="#f4f4f0" stroke-width="3"/></svg>
<div class="abs services">
  <div class="service"><svg width="28" height="28" viewBox="0 0 28 28" fill="none" stroke="#eee" stroke-width="2"><path d="M3 14a11 11 0 0 1 22 0zM14 14v9a3 3 0 0 1-5 0"/></svg>POC</div>
  <div class="service"><svg width="28" height="28" viewBox="0 0 28 28" fill="none" stroke="#eee" stroke-width="2"><path d="M5 5l8 8M13 13l9 11M20 4l-6 6 4 4 6-6"/></svg>Build product</div>
  <div class="service"><svg width="28" height="28" viewBox="0 0 28 28" fill="none" stroke="#eee" stroke-width="2"><circle cx="9" cy="9" r="4"/><circle cx="20" cy="18" r="4"/><path d="M12 12l5 3"/></svg>Maintain product</div>
  <div class="service"><svg width="28" height="28" viewBox="0 0 28 28" fill="none" stroke="#eee" stroke-width="2"><circle cx="14" cy="14" r="5"/><path d="M14 2v5M14 21v5M2 14h5M21 14h5M6 6l3 3M19 19l3 3M22 6l-3 3M6 22l3-3"/></svg>ODC setup</div>
  <div class="service"><svg width="28" height="28" viewBox="0 0 28 28" fill="none" stroke="#eee" stroke-width="2"><circle cx="14" cy="15" r="11"/><path d="M14 4v11l6 4"/></svg>Architectural interventions</div>
  <div class="service"><svg width="28" height="28" viewBox="0 0 28 28" fill="none" stroke="#eee" stroke-width="2"><path d="M17 3L9 15h8l-6 10"/></svg>Agile Consulting</div>
</div>

<div class="abs label" style="top:840px"><span>BACKGROUND AND EXPERTISE</span></div>
<p class="abs expertise">We are primarily server side programmers with expertise in large scale projects – be it Software development tools, Distributed software frameworks, Telecom and mediation software or Business intelligence.<br>Over the years, we have been the trusted offshore product development partner for many startups and mid sized software product companies, and have built software products from scratch.[...]</p>
<div class="abs" role="img" aria-label="Pencil sketch of an arched steel bridge" style="left:715px;top:985px;width:445px;height:185px;background:linear-gradient(180deg,#2a2a2a,#141414);border-top:2px solid #555;border-bottom:2px solid #555"></div>

<div class="abs label" style="top:1313px"><span>WORK WITH US</span></div>
<div class="abs wanted" role="img" aria-label="Aged paper notice with newspaper texture">
  <div class="wanted-title">WANTED</div>
  <p class="wanted-text">Brivolt, is an employee driven company. Many of our policies are created and improved based on employees' requests.If you are interested in working with us, do write to info@brivoltsoftware-example.com</p>
</div>
<p class="abs work">Brivolt works with startups and midsize product development companies. It uses design thinking and rigorouse software development principles to build world class products.</p>
<div class="abs btn">Read More</div>

<div class="abs label" style="top:1728px"><span>TESTIMONIAL</span></div>
<div class="abs qmark" style="left:238px">“</div>
<p class="abs quote">Tomas is officially the man! His level of professionalism and the understanding of the subject matter is the reason i will be looking forward</p>
<div class="abs qmark" style="left:950px">”</div>
<div class="abs client" style="top:1922px;font-size:16px;color:var(--paper)">HALVERN GROUP</div>
<div class="abs client" style="top:1950px;font-size:14px;color:var(--accent)">Mira Santoso</div>
<div class="abs client" style="top:1974px;font-size:13px;color:var(--paper)">PRESIDENT DIRECTOR</div>
<svg class="abs" style="left:215px;top:2078px" width="52" height="20" viewBox="0 0 52 20"><path d="M50 10H4M12 2L3 10l9 8" fill="none" stroke="#f4f4f0" stroke-width="3"/></svg>
<svg class="abs" style="left:1020px;top:2078px" width="52" height="20" viewBox="0 0 52 20"><path d="M2 10h46M40 2l9 8-9 8" fill="none" stroke="#f4f4f0" stroke-width="3"/></svg>
<div class="abs portrait" style="left:416px" role="img" aria-label="Client portrait photo"></div>
<div class="abs portrait" style="left:548px" role="img" aria-label="Client portrait photo"></div>
<div class="abs portrait" style="left:679px" role="img" aria-label="Client portrait photo"></div>

<div class="abs contact" style="left:88px">
  <div class="dot"><svg width="16" height="20" viewBox="0 0 16 20"><path d="M8 1a7 7 0 0 1 7 7c0 5-7 11-7 11S1 13 1 8a7 7 0 0 1 7-7z" fill="#222"/><circle cx="8" cy="8" r="2.5" fill="#f4f4f0"/></svg></div>
  <div><h3>Address</h3><p>Brivolt Software (C/O<br>Tallow Partners)<br>Unit 4 Larchfield Road<br>Greystane<br>Co.Kildare, Dublin Ireland</p></div>
</div>
<div class="abs contact" style="left:378px">
  <div class="dot"><svg width="18" height="18" viewBox="0 0 18 18"><path d="M4 1l3 4-2 2c1 2 4 5 6 6l2-2 4 3-2 3C8 17 1 10 1 3z" fill="#222"/></svg></div>
  <div><h3>Phone</h3><p style="line-height:18px">+353 (0)86 555 0142<br>Mon-Fri 8:00am - 8:00pm</p></div>
</div>
<div class="abs contact" style="left:666px">
  <div class="dot"><svg width="18" height="14" viewBox="0 0 18 14"><rect x="1" y="1" width="16" height="12" fill="#222"/><path d="M1 1l8 7 8-7" fill="none" stroke="#f4f4f0" stroke-width="1.5"/></svg></div>
  <div><h3>Mail</h3><p>support@brivoltsoftware-example.com.</p></div>
</div>

<div class="abs divider"></div>
<div class="abs copy">© 2005-2016 brivoltsoftware-example.com. All rights reserved.</div>

</body>
</html>
```